We need a range of stationery items designed for our active, community-orientated, out-going, all-age, family-friendly church in central Auckland, New Zealand.
We want to refresh and modernize the branding/images for Kereru Gospel Chapel itself so this image reflects who we are and our values.
Our church is located on a very busy intersection in the heart of a multi-ethnic local community. A number of churches and other groups use our site so we have branded our site as "The Meeting Pole". We have an existing logo for "The Meeting Pole" (see attached).
We would like you to design 4 items: a Letterhead, a With Compliments slip, a Business Card, and the Front Cover of our church newsletter, but we've included a request for an Email signature as an optional extra for this brief.
Organisation Details:
Name: Kereru Gospel Chapel
Postal Address: PO Box 38514, Wharenui, Auckland 1893
Email: office@kererugospel.org.nz
Phone: 09 473 5619
Web: www.kererugospel.org.nz (current website will be changed)
Position Statement: "a place of hope, belonging and worship"
Fonts:
The fonts for the "The Meeting Pole" logo are Futura Medium BT and Futura Lt BT. We would like the Futura font family used in the designs but feel free to add other fonts as appropriate (preferably True Type open source ones).
Colours:
Our current external signage colours are Dark Grey (Tolvar Coatings 'Slatewick' - RGB 57-55-53 ) and orange ( Tolvar 'Sunflare' - RGB 255-82-0 ). These are the colours for 'The Meeting Pole' which is our site. As we have other churches using our premises also we are looking to create a separate but complimentary identity for Kereru Gospel Chapel with a different colour set. We would ideally like a primary colour, a complimentary colour and an offset colour.
Design:
For the Kereru Gospel Chapel stationary we want the design to incorporate some of the elements of the 'Meeting Pole' particularly the extended 'T' device, so that we develop a separate identity but in the same family. We would like something that will look good for a number of years, rather than something that will date quickly in a year or two as fashions change.
PROJECTS
1. Letterhead
Finished size A4 (210 mm wide x 297mm tall)
This will become a template in MSWord. It will be printed in colour on our office photocopier so it must have a 5mm white border around the entire outside edge of the A4 page. "The Meeting Pole" logo needs to be incorporated in some form on the page.
2. With Compliments slip
Finished size 210 mm wide x 99 mm tall
This will be printed in colour on our office photocopier so it must have a 5mm white border around the entire outside edge of the slip. We will print these slips 3-up on an A4 page. The actual design space will be 200mm x 89mm. It is envisaged that this slip will use the same elements as the letterhead design. Please supply two versions, with and without the words "With Compliments".
3. Business Card
Finished size 90 mm wide by 55 mm tall.
This will be printed by commercial printers so colours can run to the edge of the card. Your Kereru Gospel Logo with the extended 'T' devise will need to feature on this.
4. Front Cover of Church Newsletter
Finished size 100 mm wide x 210 mm tall.
Our newsletter is printed in landscape on A4 paper and is folded twice.
It will be printed in colour on our office photocopier so it will need to have a minimum 5mm white border on all 4 sides. Attractive inviting colours preferred.
Needs to have:
- a place for the words Sunday and a date (which will change each Sunday)
- your Kereru Gospel Logo with the extended 'T' devise
- the words Sundays @ 10am
- the words ""a place of hope, belonging and worship"
- optional - "The Meeting Pole" logo (background does not need to be black)
5. Email Signature - optional extra
Not too large but something that will enable those receiving emails to instantly recognize who the email is from. Needs to include your Kereru Gospel logo, the name of the person, their position and our contact details.
Reason: We are extending the deadline on this project in order to encourage a broader range of designs, both from those who have already submitted designs and from those who are considering entering our competition. We'd love to see what you have to offer so please do submit your designs.
Re: Stationery for Kereru Gospel Chapel
Thanks to all the designers who have submitted designs for our competition so far. We have refrained from requesting a whole lot of tweaks to individual designs out of respect for your time as we understand that you are all busy professionals and that design competitions like this are just one way that you pitch for new business.
We would though like to offer some general comments on the submissions that we have seen so far. One thing that we would definitely like to arrive at via this process is to decide on a colour scheme. For this, as per the brief notes ( but possibly obscured by some of the other detail ) we want to have a primary colour and an offset colour and also an accent colour in the pallet.
Another thing that we maybe didn't make clear enough is that the colours for the identity of the site, known as The Meeting Pole, uses dark grey and orange but that we wanted to develop a separate but related identity for Kereru Gospel Chapel that meets there as we also now have other congregations that use our buildings.
One of the keys for the new identity will be the new colour pallet which we wanted to steer away from the darker tones that we used for the site branding. Therefore we would very much like to see your suggestions one or two secondary colours along with the primary brand colour if possible please.
Thank you all once again.
Kind regards

```html
<!DOCTYPE html>
<html lang="en">
<head>
<meta charset="utf-8">
<title>Kereru Gospel Chapel – Stationery</title>
<link rel="stylesheet" href="https://fonts.googleapis.com/css2?family=Jost:wght@300;400;500;600&display=swap">
<style>
  :root {
    --canvas: #e4e8e7;
    --ink: #2b2b2b;
    --paper: #ffffff;
    --screen: #24272a;
    --blue: #1f4f8f;
    --teal: #2ba28a;
    --green: #3ed36a;
    --lime: #a8d84a;
    --rose: #d0455e;
    --orange: #f08a2a;
  }
  * { box-sizing: border-box; margin: 0; padding: 0; }
  html, body { width: 1200px; height: 1000px; overflow: hidden; }
  body {
    position: relative;
    background: var(--canvas);
    font-family: "Jost", "Futura", sans-serif;
    color: var(--ink);
  }
  .piece { position: absolute; overflow: hidden; }

  /* shared pattern field */
  .pattern { position: absolute; }
  .pattern--vertical {
    background:
      radial-gradient(circle at 50% 40%, var(--orange) 0, transparent 12%),
      linear-gradient(180deg, var(--blue) 0%, var(--teal) 18%, var(--green) 38%, var(--lime) 45%, var(--green) 60%, var(--teal) 85%, var(--blue) 100%);
  }
  .pattern--cover {
    background:
      radial-gradient(ellipse 40% 18% at 85% 48%, var(--orange) 0, transparent 100%),
      radial-gradient(ellipse 60% 40% at 60% 30%, var(--lime) 0, transparent 100%),
      linear-gradient(180deg, var(--teal) 0%, var(--green) 35%, var(--green) 70%, var(--teal) 88%, var(--blue) 100%);
  }
  .pattern--slip {
    background:
      radial-gradient(circle at 40% 16%, var(--rose) 0, transparent 10%),
      radial-gradient(circle at 72% 22%, #d9d6b8 0, transparent 10%),
      linear-gradient(180deg, var(--teal) 0%, var(--green) 50%, var(--lime) 75%, var(--teal) 100%);
  }
  .pattern--card {
    background:
      radial-gradient(circle at 30% 12%, var(--rose) 0, transparent 16%),
      radial-gradient(ellipse 30% 40% at 95% 90%, var(--orange) 0, transparent 100%),
      linear-gradient(160deg, var(--teal) 0%, var(--green) 45%, var(--green) 75%, var(--teal) 100%);
  }
  .pattern--square {
    background:
      radial-gradient(circle at 30% 20%, var(--rose) 0, transparent 30%),
      linear-gradient(135deg, var(--blue) 0%, var(--teal) 40%, var(--green) 100%);
  }

  /* name set as plain text: one colour, one weight, one line */
  .org-name { font-weight: 400; line-height: 1.1; white-space: nowrap; letter-spacing: 0; }
  .org-name--light { color: var(--paper); }
  .org-name--dark { color: var(--ink); }

  /* tablet screen */
  .screen { left: 121px; top: 201px; width: 262px; height: 350px; background: var(--screen); }
  .screen .org-name { position: absolute; left: 0; right: 0; top: 160px; text-align: center; font-size: 24px; }

  /* letterhead */
  .letterhead { left: 477px; top: 37px; width: 398px; height: 560px; background: var(--paper); }
  .letterhead .pattern { left: 0; top: 0; width: 28px; height: 100%; }
  .site-name { position: absolute; left: 38px; top: 12px; font-size: 8px; font-weight: 400; letter-spacing: 0.08em; text-transform: uppercase; line-height: 1.2; }
  .letterhead .org-name { position: absolute; right: 16px; top: 12px; font-size: 14px; }
  .footer-line { position: absolute; left: 0; right: 0; text-align: center; font-size: 6px; font-weight: 600; line-height: 1.4; }
  .letterhead .footer-line { bottom: 12px; padding-left: 28px; }

  /* newsletter cover */
  .cover { left: 940px; top: 177px; width: 190px; height: 421px; background: var(--paper); }
  .cover .org-name { position: absolute; right: 10px; top: 34px; font-size: 15px; }
  .cover-dateline { position: absolute; left: 8px; right: 8px; top: 74px; display: flex; justify-content: space-between; font-size: 5.5px; }
  .cover .pattern { left: 0; top: 83px; width: 100%; height: 338px; }
  .statement { color: var(--paper); text-align: center; font-weight: 400; line-height: 1.2; }
  .cover .statement { position: absolute; left: 0; right: 0; bottom: 36px; font-size: 14.5px; }

  /* compliments slip */
  .slip { left: 87px; top: 650px; width: 423px; height: 188px; }
  .slip .pattern { inset: 0; }
  .slip .org-name { position: absolute; left: 9px; top: 20px; font-size: 15px; }
  .slip-note { position: absolute; left: 8px; top: 57px; width: 406px; height: 113px; background: var(--paper); }
  .slip-note h2 { font-size: 10px; font-weight: 600; padding: 4px 4px; }
  .slip .footer-line { bottom: 5px; color: var(--paper); font-size: 5.5px; }

  /* business card */
  .card { left: 547px; width: 219px; height: 141px; }
  .card--front { top: 651px; }
  .card--front .pattern { inset: 0; }
  .card--front .statement { position: absolute; left: 0; right: 0; top: 56px; font-size: 12px; font-weight: 600; }
  .card--back { top: 817px; }
  .card--back .pattern { inset: 0; }
  .card-inner { position: absolute; left: 6px; top: 5px; right: 6px; bottom: 6px; background: var(--paper); }
  .card--back .org-name { position: absolute; right: 10px; top: 12px; font-size: 11px; }
  .card--back .footer-line { bottom: 6px; font-size: 6px; }

  /* email signature */
  .signature { left: 808px; top: 652px; width: 187px; height: 56px; background: var(--paper); }
  .signature .pattern { left: 0; top: 0; width: 50px; height: 56px; }
  .signature .org-name { position: absolute; left: 4px; top: 20px; font-size: 7.5px; white-space: normal; width: 44px; }
  .signature-details { position: absolute; left: 55px; top: 4px; font-size: 4.2px; line-height: 1.35; }
  .signature-details .person { font-size: 7.5px; line-height: 1.2; }
</style>
</head>
<body>

  <section class="piece screen" aria-label="Screen identity">
    <p class="org-name org-name--light">Kereru Gospel Chapel</p>
  </section>

  <section class="piece letterhead" aria-label="Letterhead">
    <div class="pattern pattern--vertical" role="img" aria-label="Vertical band of colourful geometric pattern in blue, green and orange"></div>
    <div class="site-name">The<br>Meeting Pole</div>
    <p class="org-name org-name--dark">Kereru Gospel Chapel</p>
    <p class="footer-line">Kereru Gospel Chapel | PO Box 38514, Wharenui, Auckland 1893 | 09 473 5619<br>office@kererugospel.org.nz | www.kererugospel.org.nz</p>
  </section>

  <section class="piece cover" aria-label="Newsletter front cover">
    <p class="org-name org-name--dark">Kereru Gospel Chapel</p>
    <div class="cover-dateline"><span>Sunday @ 10:00am</span><span>Sunday 05 October 2014</span></div>
    <div class="pattern pattern--cover" role="img" aria-label="Colourful geometric pattern in green with orange and blue tones"></div>
    <p class="statement">"a place of hope,<br>belonging and worship"</p>
  </section>

  <section class="piece slip" aria-label="With compliments slip">
    <div class="pattern pattern--slip" role="img" aria-label="Colourful geometric pattern in teal, green and rose"></div>
    <p class="org-name org-name--light">Kereru Gospel Chapel</p>
    <div class="slip-note"><h2>With Compliments</h2></div>
    <p class="footer-line">Kereru Gospel Chapel | PO Box 38514, Wharenui, Auckland 1893 | 09 473 5619 | office@kererugospel.org.nz | www.kererugospel.org.nz</p>
  </section>

  <section class="piece card card--front" aria-label="Business card front">
    <div class="pattern pattern--card" role="img" aria-label="Colourful geometric pattern in green with rose and orange tones"></div>
    <p class="statement">"a place of hope,<br>belonging and worship"</p>
  </section>

  <section class="piece card card--back" aria-label="Business card back">
    <div class="pattern pattern--card" role="img" aria-label="Colourful geometric pattern border"></div>
    <div class="card-inner">
      <p class="org-name org-name--dark">Kereru Gospel Chapel</p>
      <p class="footer-line">PO Box 38514, Wharenui, Auckland 1893 | 09 473 5619<br>office@kererugospel.org.nz | www.kererugospel.org.nz</p>
    </div>
  </section>

  <section class="piece signature" aria-label="Email signature">
    <div class="pattern pattern--square" role="img" aria-label="Square of colourful geometric pattern"></div>
    <p class="org-name org-name--light">Kereru Gospel Chapel</p>
    <div class="signature-details">
      <p class="person">Name Surname<br>Position</p>
      <p>PO Box 38514, Wharenui, Auckland 1893<br>E: office@kererugospel.org.nz<br>P: 09 473 5619<br>W: www.kererugospel.org.nz<br>&nbsp;&nbsp;&nbsp;&nbsp;&nbsp;&nbsp;&nbsp;&nbsp;"a place of hope, belonging and worship"</p>
    </div>
  </section>

</body>
</html>
```